Multi-Line Insurance PPC Landing Page - Conversion optimized.

We have a PPC landing page used for the general population to get an insurance quote through an agent's site.

We'd like to improve the page for PPC traffic, make it more conversion friendly.

Site should be a single long page.

We will dynamically change the form and headlines on the page depending on what insurance "line" is being called. ie, Lift, Auto, Home, Business.

The enclosed AI file has all of the raw elements we need. We're looking to enhance the design and conversion ability.

Target Market(s)

General public needed insurance services.

Industry/Entity Type

Insurance Broker

Number of Pages Required

1 page

Font styles to use
Sans Serif

Requirements
Must have
• Form, agent picture, name, address.

```html
<!DOCTYPE html>
<html lang="en">
<head>
<meta charset="utf-8">
<title>Insurance Agent – Get a Quote</title>
<link href="https://fonts.googleapis.com/css2?family=Open+Sans:wght@400;600;700;800&display=swap" rel="stylesheet">
<style>
:root{
  --green:#2fb24a;
  --green-dark:#23913a;
  --blue:#1d5ea8;
  --navy:#0d2d5e;
  --navy-deep:#081f44;
  --ink:#333a44;
  --muted:#8a9099;
  --line:#d9dde2;
  --panel:#eef0f2;
  --white:#fff;
}
*{box-sizing:border-box;margin:0;padding:0}
html,body{width:784px;height:1200px;overflow:hidden}
body{font-family:"Open Sans",Arial,sans-serif;color:var(--ink);background:var(--white);position:relative}

/* header */
.site-header{height:44px;display:flex;align-items:center;justify-content:space-between;padding:0 26px 0 22px;background:var(--white)}
.brand{display:flex;align-items:center;gap:6px;font-weight:800;font-size:17px;color:var(--green);letter-spacing:.5px;text-transform:uppercase}
.brand-mark{width:12px;height:12px;background:var(--green)}
.header-actions{display:flex;align-items:center;gap:14px}
.btn{display:inline-block;background:var(--green);color:var(--white);font-weight:700;text-transform:uppercase;border-radius:2px;text-align:center}
.btn-small{font-size:10px;padding:6px 10px}
.phone{display:flex;align-items:center;gap:6px;font-size:15px;font-weight:600;color:var(--ink)}

/* hero */
.hero{position:relative;height:241px;overflow:hidden}
.hero-photo{position:absolute;inset:0;background:linear-gradient(100deg,#c9a878 0%,#e9dcc6 28%,#f4f1ec 45%,#3b3f47 62%,#1e2128 100%)}
.hero-arrow{position:absolute;top:100px}
.hero-arrow.prev{left:14px}.hero-arrow.next{right:14px}
.hero-band{position:absolute;left:145px;bottom:14px;display:flex;align-items:center;gap:14px}
.hero-title{font-size:34px;font-weight:800;color:var(--white);background:rgba(20,24,32,.55);padding:2px 14px;letter-spacing:.3px}
.btn-hero{font-size:15px;padding:11px 14px;border:2px solid rgba(255,255,255,.7)}

/* quote */
.quote{height:280px;padding-top:18px}
.section-title{text-align:center;font-size:23px;font-weight:800;text-transform:uppercase;letter-spacing:.3px}
.section-title.green{color:var(--green)}
.section-title.blue{color:var(--blue)}
.section-sub{text-align:center;font-size:11px;color:var(--muted);margin-top:4px}
.quote-body{display:flex;width:660px;margin:14px auto 0;box-shadow:0 2px 6px rgba(0,0,0,.12)}
.agent-card{width:200px;background:var(--white);position:relative;text-align:center;padding-bottom:10px}
.agent-banner{height:60px;background:linear-gradient(135deg,#cfd4da,#eef0f2 60%,#b8c2cc)}
.agent-photo{width:74px;height:74px;border-radius:50%;border:4px solid var(--green);background:linear-gradient(180deg,#9aa4ae,#3a4450);margin:-42px auto 0;position:relative}
.agent-name{font-size:12px;font-weight:700;margin-top:6px}
.agent-address{font-size:9px;color:var(--muted);line-height:1.45;margin-top:3px}
.agent-phone{font-size:9px;color:var(--blue);font-weight:600;margin-top:3px}
.quote-form{flex:1;background:var(--panel);padding:10px 16px 12px;display:grid;grid-template-columns:1fr 1fr;column-gap:14px;row-gap:5px}
.field label{display:block;font-size:8px;color:var(--muted);margin-bottom:2px}
.input{height:15px;background:var(--white);border:1px solid var(--line)}
.split{display:flex;gap:4px}.split .input{flex:1}
.field.full{grid-column:1/3}
.btn-submit{grid-column:2;font-size:10px;padding:5px 0;margin-top:3px}

/* about */
.about{height:125px;padding:18px 70px 0}
.about p{font-size:9.5px;line-height:1.6;color:var(--muted);text-align:center;margin-top:10px}

/* products */
.products{height:275px;background:var(--white);padding-top:4px}
.product-grid{display:flex;justify-content:space-between;width:650px;margin:22px auto 0}
.product{width:140px;text-align:center}
.product-icon{width:70px;height:70px;margin:0 auto;border-radius:50%;border:4px solid var(--line);border-top-color:var(--blue);border-left-color:var(--blue);display:flex;align-items:center;justify-content:center}
.product h3{font-size:13px;font-weight:800;text-transform:uppercase;margin-top:10px}
.product p{font-size:8.5px;line-height:1.55;color:var(--muted);margin-top:5px;min-height:54px}
.product .btn{font-size:9px;padding:5px 12px;margin-top:6px}

/* reviews */
.reviews{height:175px;background:#f6f7f8;padding-top:16px}
.review{display:flex;gap:16px;width:640px;margin:16px auto 0;align-items:flex-start}
.reviewer-photo{flex:none;width:46px;height:46px;border-radius:50%;background:linear-gradient(180deg,#d8b89a,#8a6a52)}
.review-text{font-size:9.5px;line-height:1.6;color:var(--muted);font-style:italic}
.review-name{font-size:10px;font-weight:700;color:var(--ink);margin-top:6px}
.dots{display:flex;gap:5px;justify-content:center;margin-top:8px}
.dot{width:7px;height:7px;border-radius:50%;background:var(--line)}
.dot.active{background:var(--blue)}

/* footer */
.disclaimer{height:42px;background:var(--navy);color:#c9d4e6;font-size:8.5px;line-height:1.5;padding:8px 70px;text-align:center}
.disclaimer strong{color:var(--white)}
.copyright{height:18px;background:var(--navy-deep);color:#9fb0cc;font-size:8px;text-align:center;line-height:18px}
</style>
</head>
<body>

<header class="site-header">
  <div class="brand"><span class="brand-mark"></span>Insurance Agent</div>
  <div class="header-actions">
    <span class="btn btn-small">Get a Quote!</span>
    <span class="phone">
      <svg width="14" height="14" viewBox="0 0 24 24"><path fill="#2fb24a" d="M6.6 10.8a15.1 15.1 0 0 0 6.6 6.6l2.2-2.2a1 1 0 0 1 1-.25 11.4 11.4 0 0 0 3.6.57 1 1 0 0 1 1 1V20a1 1 0 0 1-1 1A17 17 0 0 1 3 4a1 1 0 0 1 1-1h3.5a1 1 0 0 1 1 1c0 1.25.2 2.45.57 3.57a1 1 0 0 1-.25 1z"/></svg>
      012-555-0147
    </span>
  </div>
</header>

<section class="hero">
  <div class="hero-photo" role="img" aria-label="Business people shaking hands over a row of falling dominoes held back by a hand"></div>
  <svg class="hero-arrow prev" width="16" height="30" viewBox="0 0 16 30"><path d="M13 3 3 15l10 12" fill="none" stroke="#fff" stroke-width="3"/></svg>
  <svg class="hero-arrow next" width="16" height="30" viewBox="0 0 16 30"><path d="m3 3 10 12L3 27" fill="none" stroke="#fff" stroke-width="3"/></svg>
  <div class="hero-band">
    <h1 class="hero-title">Protection Plan</h1>
    <span class="btn btn-hero">Get a Quick Quote !</span>
  </div>
</section>

<section class="quote">
  <h2 class="section-title green">Get an Instant Insurance Quote.</h2>
  <p class="section-sub">A fast and secure way to get a quote quickly.</p>
  <div class="quote-body">
    <div class="agent-card">
      <div class="agent-banner" role="img" aria-label="Office backdrop behind the agent"></div>
      <div class="agent-photo" role="img" aria-label="Portrait of the insurance agent"></div>
      <div class="agent-name">Owen Harlow - Agent</div>
      <div class="agent-address">4820 Maple Ave, Suite 210<br>Fairview, CA 90210</div>
      <div class="agent-phone">(012) 555-0198</div>
    </div>
    <form class="quote-form">
      <div class="field full"><label>What type of insurance are you interested in?</label><div class="input"></div></div>
      <div class="field"><label>First Name</label><div class="input"></div></div>
      <div class="field"><label>Street Address</label><div class="input"></div></div>
      <div class="field"><label>Last Name</label><div class="input"></div></div>
      <div class="field"><label>City / State</label><div class="input"></div></div>
      <div class="field"><label>Date of Birth</label><div class="split"><div class="input"></div><div class="input"></div><div class="input"></div></div></div>
      <div class="field"><label>Phone</label><div class="input"></div></div>
      <div class="field"><label>Gender</label><div class="input"></div></div>
      <div class="field"><label>Email</label><div class="input"></div></div>
      <span class="btn btn-submit">Submit</span>
    </form>
  </div>
</section>

<section class="about">
  <h2 class="section-title blue">About Insurance Agent</h2>
  <p>We are an independent agency helping families and business owners find coverage that fits their needs and budget. Our licensed agents compare plans from trusted carriers, explain every option in plain language and stay with you long after the policy is signed, so claims, renewals and questions are always handled quickly and personally.</p>
</section>

<section class="products">
  <h2 class="section-title green">Our Insurance Products</h2>
  <div class="product-grid">
    <div class="product">
      <div class="product-icon">
        <svg width="34" height="30" viewBox="0 0 34 30"><rect x="4" y="10" width="14" height="12" fill="#1d5ea8"/><rect x="20" y="2" width="3" height="20" fill="#1d5ea8"/><rect x="23" y="19" width="10" height="3" fill="#1d5ea8"/><circle cx="8" cy="25" r="3.5" fill="#0d2d5e"/><circle cx="17" cy="25" r="3.5" fill="#0d2d5e"/></svg>
      </div>
      <h3>Lift</h3>
      <p>Protect the people who depend on you with flexible term and whole life coverage options.</p>
      <span class="btn">Get a Quote</span>
    </div>
    <div class="product">
      <div class="product-icon">
        <svg width="36" height="24" viewBox="0 0 36 24"><path d="M3 16v-5l5-1 5-6h11l6 6 4 1v5z" fill="#1d5ea8"/><circle cx="10" cy="18" r="4" fill="#0d2d5e"/><circle cx="27" cy="18" r="4" fill="#0d2d5e"/></svg>
      </div>
      <h3>Auto</h3>
      <p>Affordable car coverage with liability, collision and roadside help for every driver in your home.</p>
      <span class="btn">Get a Quote</span>
    </div>
    <div class="product">
      <div class="product-icon">
        <svg width="32" height="30" viewBox="0 0 32 30"><path d="M16 2 2 14h4v14h8v-9h4v9h8V14h4z" fill="#1d5ea8"/></svg>
      </div>
      <h3>Home</h3>
      <p>Cover your house, belongings and liability against fire, theft, storms and unexpected accidents at home.</p>
      <span class="btn">Get a Quote</span>
    </div>
    <div class="product">
      <div class="product-icon">
        <svg width="32" height="28" viewBox="0 0 32 28"><rect x="11" y="2" width="10" height="6" fill="none" stroke="#0d2d5e" stroke-width="3"/><rect x="2" y="8" width="28" height="18" rx="2" fill="#1d5ea8"/><rect x="2" y="14" width="28" height="2" fill="#0d2d5e"/></svg>
      </div>
      <h3>Business</h3>
      <p>Keep your company running with property, liability and workers coverage built around your trade.</p>
      <span class="btn">Get a Quote</span>
    </div>
  </div>
</section>

<section class="reviews">
  <h2 class="section-title green">Client Reviews</h2>
  <div class="review">
    <div class="reviewer-photo" role="img" aria-label="Portrait of a smiling client"></div>
    <div>
      <p class="review-text">“The agent made switching my policies simple. He compared several carriers, found me better coverage for less money and answered every question I had. I now recommend this office to all my friends and family members.”</p>
      <div class="review-name">- Ms. Dana Whitfield</div>
    </div>
  </div>
  <div class="dots"><span class="dot active"></span><span class="dot"></span><span class="dot"></span></div>
</section>

<footer>
  <div class="disclaimer"><strong>Disclaimer :</strong> Coverage availability, rates and discounts vary by state and carrier. Quotes are estimates only and are subject to underwriting approval. Submitting this form does not bind any policy.</div>
  <div class="copyright">© 2016 Insurance Agent | All Rights Reserved</div>
</footer>

</body>
</html>
```